Hello ,this is a clothing webshop for my Brand,I'm trying to sell 6 designs a month to start which consists of hoodies ,T-shirts and hats..I'm supper webshop illiterate but due to me placing orders and visiting other webshops i know roughly what id like so I'll just go down the list for you.i might seem all over the place but here goes...I'd like to have my logo on it you can make it slightly different if you'd like but not far deviated and you can make it whatever color you'd like you don't have to copy my example foto's however i would like Lucien to be written in script above Ka'Romu ..I'd like to have spots to add people modeling my peices I'd like an about me or my story section,links to my social media and email ,space for my contact info and adress, I'd like all the traditional options every clothing site has a feed back slot maybe also with picture post of them wearingthe item,an option to leave your email to receive launch notification and back instock notification ect.., I'd like my customers to track their order and send msg,I'd like to be able to check algorithms be placed in the top of Google search engines I'll download an example of a simple site i visited recently that i like as an example and if you need anything else from me feel free to ask,i respond fast.guys go check out that website i uploaded ..thank you very much
For now its urban
Clothing

```html
<!DOCTYPE html>
<html lang="en">
<head>
<meta charset="utf-8">
<title>Ka'Romu — Urban Clothing</title>
<link href="https://fonts.googleapis.com/css2?family=Poppins:ital,wght@0,400;0,500;0,600;0,700;0,800;1,400;1,600&family=Lato:wght@400;700&display=swap" rel="stylesheet">
<style>
:root{
  --green:#8dc63f;
  --ink:#1e1e1e;
  --dark:#222222;
  --footer:#2b2b2b;
  --topbar:#333333;
  --grey-bg:#f2f2f2;
  --text:#444444;
  --white:#ffffff;
}
*{margin:0;padding:0;box-sizing:border-box}
html,body{width:1200px;height:3904px;overflow:hidden}
body{position:relative;font-family:'Poppins',sans-serif;color:var(--text);background:var(--white)}
.abs{position:absolute}
.photo{position:absolute;display:block}

.topbar{left:0;top:0;width:1200px;height:36px;background:var(--topbar);color:#eee;font-family:'Lato',sans-serif;font-size:13px;letter-spacing:.5px;display:flex;justify-content:center;align-items:center;gap:22px}
.topbar span{display:flex;align-items:center;gap:8px}

.brand{left:76px;top:74px;display:flex;align-items:center;gap:14px;font-weight:800;font-size:44px;color:var(--green);letter-spacing:1px;white-space:nowrap}
.brand .dot{width:34px;height:34px;background:var(--green);border-radius:50%}
.currency{left:830px;top:60px;width:64px;height:30px;border:1px solid #ccc;font-size:11px;display:flex;align-items:center;justify-content:center;gap:10px;color:#333}
.search{left:903px;top:60px;width:223px;height:30px;border:1px solid #ccc;font-size:11px;color:#333;display:flex;align-items:center;justify-content:space-between;padding:0 8px}
.nav{left:508px;top:126px;font-size:14.5px;font-weight:500}
.nav a{position:absolute;white-space:nowrap;text-decoration:none;color:#333}
.nav a.active{color:var(--green)}
.cart{left:1071px;top:118px;width:36px;height:36px;border-radius:50%;background:var(--green);display:flex;align-items:center;justify-content:center}
.cart-count{left:1106px;top:112px;font-size:15px;color:#333}

.hero{left:0;top:176px;width:1200px;height:629px;background:linear-gradient(100deg,#c9c4bc 0%,#9b948c 35%,#3a3633 62%,#1f1d1c 100%)}
.hero-box{left:76px;top:358px;width:592px;height:240px;background:rgba(255,255,255,.82)}
.hero-title{left:92px;top:380px;width:576px;font-size:52px;font-weight:800;color:var(--ink);letter-spacing:.5px;white-space:nowrap}
.hero-text{left:96px;top:446px;width:560px;font-size:17px;line-height:27px;color:#333;font-family:'Lato',sans-serif}
.btn{position:absolute;background:var(--green);color:var(--white);font-weight:600;font-size:14px;letter-spacing:.5px;display:flex;align-items:center;justify-content:center;text-transform:uppercase}
.dots{left:74px;top:745px;display:flex;gap:10px}
.dots i{width:16px;height:16px;border-radius:50%;background:#8a8580;display:block}
.dots i.on{background:#222}

.promo-new{left:74px;top:844px;width:331px;height:500px;background:var(--green);color:var(--white);text-align:center}
.promo-new h2{position:absolute;left:0;top:52px;width:100%;font-size:51px;font-weight:800;line-height:54px;letter-spacing:1px}
.promo-new .upto{position:absolute;left:0;top:170px;width:100%;font-size:25px;font-style:italic;font-weight:600}
.promo-new .off{position:absolute;left:0;top:206px;width:100%;font-size:52px;font-weight:800;color:var(--ink)}
.promo-new p{position:absolute;left:30px;top:278px;width:271px;font-size:15px;line-height:28px}
.promo-new .outline{position:absolute;left:94px;top:388px;width:152px;height:51px;border:2px solid var(--white);font-size:14px;font-weight:600;display:flex;align-items:center;justify-content:center}
.tile-label{position:absolute;font-weight:800;color:var(--ink);letter-spacing:1px}
.tile-link{position:absolute;font-size:14px;font-weight:600;color:var(--ink);text-decoration:underline;text-underline-offset:4px}

.featured{left:0;top:1406px;width:1200px;height:602px;background:var(--grey-bg)}
.section-title{position:absolute;left:0;width:1200px;text-align:center;font-weight:800;color:var(--ink);letter-spacing:1px}
.card{position:absolute;top:1568px;width:240px;height:417px;background:var(--white)}
.card .img{position:absolute;left:0;top:0;width:240px;height:338px}
.card .name{position:absolute;left:0;top:344px;width:100%;text-align:center;font-size:15px;font-weight:500;color:#222}
.card .price{position:absolute;left:0;top:372px;width:100%;text-align:center;font-size:15px;color:var(--green)}
.arrow{position:absolute}

.banner{left:0;top:2070px;width:1200px;height:343px;background:var(--dark)}
.banner-img{left:636px;top:2070px;width:564px;height:343px;background:linear-gradient(90deg,#2a2a2a 0%,#6a6a6a 25%,#8e8e8e 60%,#5a5a5a 100%)}
.banner-title{left:74px;top:2146px;font-size:52px;line-height:56px;font-weight:800;color:var(--white);letter-spacing:1px}
.banner-links{left:84px;top:2293px;font-size:14px;font-weight:700;color:var(--white);letter-spacing:.5px}

.about-title{left:615px;top:2466px;font-size:47px;font-weight:800;color:var(--ink);letter-spacing:1px;white-space:nowrap}
.about-title span{color:var(--green)}
.about-text{left:616px;top:2543px;width:515px;font-size:16px;line-height:27.7px;color:#444}

.news{left:0;top:2892px;width:600px;height:285px;background:var(--green)}
.news h2{position:absolute;left:74px;top:60px;font-size:38px;font-weight:800;color:var(--white);letter-spacing:1px}
.news p{position:absolute;left:74px;top:118px;font-size:16px;color:var(--white);font-family:'Lato',sans-serif}
.news .field{position:absolute;left:74px;top:168px;width:337px;height:45px;background:var(--white);font-size:13px;color:#333;display:flex;align-items:center;padding-left:16px;font-family:'Lato',sans-serif}
.news .go{position:absolute;left:424px;top:168px;width:103px;height:45px;background:var(--dark);color:var(--white);font-size:14px;font-weight:600;display:flex;align-items:center;justify-content:center}
.reviews{left:600px;top:2892px;width:600px;height:285px;background:var(--dark)}
.reviews h2{position:absolute;left:30px;top:38px;font-size:36px;font-weight:800;color:var(--white);letter-spacing:1px}
.reviews .quote{position:absolute;left:180px;top:104px;width:340px;font-size:16px;line-height:28px;color:#eee;font-style:italic}
.reviews .who{position:absolute;left:180px;top:220px;font-size:14px;font-weight:700;color:var(--green)}

.footer{left:0;top:3568px;width:1200px;height:336px;background:var(--footer);color:#eee}
.footer .brand-f{position:absolute;left:74px;top:52px;display:flex;align-items:center;gap:14px;font-size:42px;font-weight:800;color:var(--white);letter-spacing:1px}
.footer .brand-f .dot{width:32px;height:32px;border-radius:50%;background:var(--white)}
.footer .about-f{position:absolute;left:74px;top:160px;width:300px;font-size:15px;line-height:26px;color:#ddd}
.fcol{position:absolute;top:50px}
.fcol h4{font-size:15.5px;font-weight:700;color:var(--green);letter-spacing:.5px;margin-bottom:14px}
.fcol li{list-style:none;font-size:15.5px;color:#eee;line-height:26px;margin-bottom:14px}
.fcol.contact li{margin-bottom:8px}
.footer .rule{position:absolute;left:74px;top:280px;width:1053px;height:1px;background:#444}
.footer .copy{position:absolute;left:74px;top:300px;font-size:13.5px;color:#ddd}
.social{position:absolute;left:972px;top:298px;display:flex;gap:14px}
.social i{display:block;width:20px;height:20px;border-radius:50%;background:#eee}
</style>
</head>
<body>

<div class="abs topbar">
  <span><svg width="18" height="13" viewBox="0 0 18 13"><rect x="0" y="1" width="11" height="8" fill="#eee"/><path d="M11 4h4l3 3v2h-7z" fill="#eee"/><circle cx="4" cy="11" r="2" fill="#eee"/><circle cx="14" cy="11" r="2" fill="#eee"/></svg>FREE SHIPPING</span>
  <span>|</span>
  <span><svg width="15" height="13" viewBox="0 0 15 13"><path d="M5 1L1 5l4 4V6.5c4 0 7 1 9 5-1-5-4-8-9-8z" fill="#eee"/></svg>FREE RETURNS.</span>
</div>

<header>
  <div class="abs brand"><span class="dot"></span>KA'ROMU</div>
  <div class="abs currency">USD <svg width="8" height="6" viewBox="0 0 8 6"><path d="M1 1l3 3 3-3" stroke="#333" fill="none" stroke-width="1.2"/></svg></div>
  <div class="abs search">Search <svg width="14" height="14" viewBox="0 0 14 14"><circle cx="6" cy="6" r="4.5" stroke="#111" stroke-width="2" fill="none"/><path d="M9.5 9.5L13 13" stroke="#111" stroke-width="2"/></svg></div>
  <nav class="abs nav">
    <a class="active" style="left:0">HOME</a>
    <a style="left:80px">PRODUCTS</a>
    <a style="left:194px">BLOG</a>
    <a style="left:263px">SHOP</a>
    <a style="left:341px">REVIEWS</a>
    <a style="left:440px">CONTACT US</a>
  </nav>
  <div class="abs cart"><svg width="16" height="14" viewBox="0 0 16 14"><path d="M0 1h3l2 8h8l2-6H4" stroke="#fff" stroke-width="1.8" fill="none"/><circle cx="6" cy="12" r="1.4" fill="#fff"/><circle cx="12" cy="12" r="1.4" fill="#fff"/></svg></div>
  <div class="abs cart-count">(0)</div>
</header>

<section>
  <div class="photo hero" role="img" aria-label="Bearded man in a beanie and black brand hoodie on a city street"></div>
  <div class="abs hero-box"></div>
  <h1 class="abs hero-title">WELCOME KA'ROMU</h1>
  <p class="abs hero-text">Sed ut perspiciatis unde omnis iste natus error sit voluptatem accusa<br>ntium doloremque laudantium, totam rem aperiam, eaque ipsa qu<br>ae ab illo inventore veritatis et quasi architecto.</p>
  <div class="btn" style="left:94px;top:541px;width:152px;height:51px">Shop Now</div>
  <div class="abs dots"><i class="on"></i><i></i><i></i><i></i></div>
</section>

<section>
  <div class="abs promo-new">
    <h2>NEW<br>ARRIVALS</h2>
    <div class="upto">Get Upto</div>
    <div class="off">40% OFF</div>
    <p>Sed ut perspiciatis unde omnis iste natus error sit voluptatem accusantium eiusmod tempor.</p>
    <div class="outline">SHOP NOW</div>
  </div>

  <div class="photo" style="left:433px;top:844px;width:694px;height:235px;background:linear-gradient(90deg,#b9b9c9 0%,#c4c3d2 45%,#d9a9c4 75%,#c6c5d3 100%)" role="img" aria-label="Young man in glasses wearing a pink brand hoodie"></div>
  <div class="tile-label" style="left:464px;top:912px;font-size:42px">HOODIES</div>
  <div class="tile-link" style="left:466px;top:978px">SHOP NOW</div>

  <div class="photo" style="left:433px;top:1108px;width:334px;height:236px;background:linear-gradient(90deg,#c9c9c9 0%,#bdbdbd 55%,#3a3a3a 100%)" role="img" aria-label="Smiling man in a black brand T-shirt against a brick wall"></div>
  <div class="tile-label" style="left:443px;top:1176px;font-size:43px">T-SHIRT</div>
  <div class="tile-link" style="left:445px;top:1244px">SHOP NOW</div>

  <div class="photo" style="left:794px;top:1108px;width:333px;height:236px;background:linear-gradient(90deg,#b08e6e 0%,#d2b9a0 40%,#e3dcd6 75%,#cfc8c2 100%)" role="img" aria-label="Laughing woman in a straw hat and sunglasses"></div>
  <div class="tile-label" style="left:997px;top:1176px;font-size:43px">HATS</div>
  <div class="tile-link" style="left:1032px;top:1244px">SHOP NOW</div>
</section>

<section>
  <div class="abs featured"></div>
  <h2 class="section-title" style="top:1480px;font-size:46px">FEATURED PRODUCTS</h2>

  <svg class="arrow" style="left:46px;top:1764px" width="14" height="26" viewBox="0 0 14 26"><path d="M12 2L2 13l10 11" stroke="#555" stroke-width="2" fill="none"/></svg>
  <svg class="arrow" style="left:1140px;top:1764px" width="14" height="26" viewBox="0 0 14 26"><path d="M2 2l10 11L2 24" stroke="#555" stroke-width="2" fill="none"/></svg>

  <div class="card" style="left:74px">
    <div class="photo img" style="background:linear-gradient(180deg,#fff 0%,#f3f3f3 15%,#3a3a3a 45%,#4a4a4a 100%)" role="img" aria-label="Man modelling a black brand hoodie and grey jeans"></div>
    <div class="name">Pellentesque Habitant</div><div class="price">$15.00</div>
  </div>
  <div class="card" style="left:345px">
    <div class="photo img" style="background:linear-gradient(180deg,#fff 0%,#f4f1ef 20%,#ececec 55%,#5b7395 100%)" role="img" aria-label="Woman modelling a white brand T-shirt and jeans"></div>
    <div class="name">Pellentesque Habitant</div><div class="price">$15.00</div>
  </div>
  <div class="card" style="left:617px">
    <div class="photo img" style="background:linear-gradient(180deg,#fff 0%,#f1f1f1 15%,#e9b8cf 50%,#f0c4d8 100%)" role="img" aria-label="Man modelling a pink brand hoodie"></div>
    <div class="name">Pellentesque Habitant</div><div class="price">$15.00</div>
  </div>
  <div class="card" style="left:888px">
    <div class="photo img" style="background:linear-gradient(180deg,#fff 0%,#f1e8e6 15%,#d44a4a 55%,#2c2c2c 100%)" role="img" aria-label="Woman modelling a red brand cap with a plaid shirt"></div>
    <div class="name">Pellentesque Habitant</div><div class="price">$15.00</div>
  </div>
</section>

<section>
  <div class="abs banner"></div>
  <div class="photo banner-img" role="img" aria-label="Man in glasses and beanie wearing a grey brand hoodie before a patterned wall"></div>
  <h2 class="abs banner-title">6 NEW DESIGNS FOR<br>EVERY MONTH</h2>
  <div class="abs banner-links">HOODIES &nbsp;&nbsp;|&nbsp;&nbsp; T-SHIRTS &nbsp;&nbsp;|&nbsp;&nbsp; HATS</div>
  <div class="btn" style="left:368px;top:2279px;width:153px;height:50px">Shop Now</div>
</section>

<section>
  <div class="photo" style="left:74px;top:2480px;width:512px;height:338px;background:linear-gradient(180deg,#c7c9cb 0%,#a9acae 45%,#202020 70%,#151515 100%)" role="img" aria-label="Couple in sunglasses wearing matching black brand hoodies"></div>
  <h2 class="abs about-title">ABOUT <span>Ka'Romu</span></h2>
  <p class="abs about-text">Sed ut perspiciatis unde omnis iste natus error sit voluptatem accusantium doloremque laudantium, totam rem aperiam, eaque ipsa quae ab illo inventore veritatis et quasi architecto beatae vitae dicta sunt explicabo. Nemo enim ipsam voluptatem quia voluptas sit aspernatur aut odit aut fugit, sed quia consequuntur magni dolores eos qui ratione voluptatem sequi nesciunt.</p>
  <div class="btn" style="left:615px;top:2766px;width:153px;height:51px">Read More</div>
</section>

<section>
  <div class="abs news">
    <h2>NEWSLETTER SIGN UP</h2>
    <p>Receive updates, access to exclusive deals, and more.</p>
    <div class="field">Enter Email Address</div>
    <div class="go">SIGN UP</div>
  </div>
  <div class="abs reviews">
    <h2>REVIEWS</h2>
    <svg style="position:absolute;left:466px;top:44px" width="14" height="26" viewBox="0 0 14 26"><path d="M12 2L2 13l10 11" stroke="#fff" stroke-width="2.5" fill="none"/></svg>
    <svg style="position:absolute;left:512px;top:44px" width="14" height="26" viewBox="0 0 14 26"><path d="M2 2l10 11L2 24" stroke="#8dc63f" stroke-width="2.5" fill="none"/></svg>
    <div class="photo" style="left:30px;top:111px;width:129px;height:127px;border-radius:8px;background:linear-gradient(180deg,#e6e6e6 0%,#d8c9a8 35%,#1d1d1d 70%)" role="img" aria-label="Customer wearing a black brand T-shirt"></div>
    <p class="quote">“ Sed ut perspiciatis unde omnis iste natus error sit voluptatem &nbsp;accusantium dolo emque laudantium, totam rem aperiam, eaque ipsa quae..”</p>
    <div class="who">NAME HEADING</div>
  </div>
</section>

<section>
  <h2 class="section-title" style="top:3228px;font-size:29px">INSTAGRAM</h2>
  <div class="photo" style="left:74px;top:3292px;width:210px;height:203px;background:linear-gradient(160deg,#c98f6a 0%,#2a2a2a 55%,#5b3a2a 100%)" role="img" aria-label="Hands holding a black brand cap"></div>
  <div class="photo" style="left:285px;top:3292px;width:210px;height:203px;background:linear-gradient(90deg,#3a3a3a 0%,#a8aeb4 50%,#3a3a3a 100%)" role="img" aria-label="Man in a grey brand hoodie before a patterned wall"></div>
  <div class="photo" style="left:496px;top:3292px;width:210px;height:203px;background:linear-gradient(180deg,#b9bbbd 0%,#1c1c1c 60%)" role="img" aria-label="Couple in black brand hoodies"></div>
  <div class="photo" style="left:707px;top:3292px;width:210px;height:203px;background:linear-gradient(180deg,#e9e6e2 0%,#d6c7a4 40%,#f4f4f4 80%)" role="img" aria-label="Woman in a brand cap and white T-shirt"></div>
  <div class="photo" style="left:917px;top:3292px;width:210px;height:203px;background:linear-gradient(180deg,#e8e8e8 0%,#d9c7a1 35%,#1e1e1e 70%)" role="img" aria-label="Woman in a black brand T-shirt"></div>
</section>

<footer class="abs footer">
  <div class="brand-f"><span class="dot"></span>KA'ROMU</div>
  <p class="about-f">Cras non dolor eu nisi dignissim pret ium. Praesent neque arcu, commodo et suscipit ut, bibendum non ipsum.</p>
  <div class="fcol" style="left:435px"><h4>MY ACCOUNT</h4><ul><li>Cras non dolor</li><li>Dignissim pretium</li><li>Praesent neque</li><li>Commodo</li></ul></div>
  <div class="fcol" style="left:650px"><h4>CUSTOMER SUPPORT</h4><ul><li>Cras non dolor</li><li>Dignissim pretium</li><li>Praesent neque</li><li>Commodo</li></ul></div>
  <div class="fcol contact" style="left:893px"><h4>CONTACT INFO</h4><ul><li>27 Hollin Lane Norwick,<br>NR7 4QB, United Kingdom</li><li>1-800-555-0182</li><li>hello@karomu-wear.com</li></ul></div>
  <div class="rule"></div>
  <div class="copy">Copyright ©2022 by Company Name All Right Reserved</div>
  <div class="social"><i></i><i></i><i></i><i></i><i></i></div>
</footer>

</body>
</html>
```